Hummingfern Bramble Dabs - our own unique product line of cotton swabs

We have something now that we are not too happy with. Looking to create a label for a line of cotton swabs that we have created and designed to clean your nose from mucus and boogers. The logo that i have so far for the packaging is the white background with the black silhouette nose (attached). We need something that can do well in the retail/consumer market. Our website address (even though it is not live yet) should be listed somewhere on the label....
www.HummingfernBramble.example ( we sell pillows, but we have other product lines)
We would also like to see a brief description on how to correctly use the nose pick on the back side of the label. The description on how to use should read " insert cotton nose pick into nostril and give it a few counter clock wise twirls or till you feel mucus/debris latch onto the cotton. You may need to repeat the process and use more than one nose pick to achieve desired result."
As well as a warning mentioning : "Never insert plastic end of nose pick into any part of your body. Be careful and use with caution."
Also for you to know, the cotton is made from 100% natural cotton, the cotton head itself is thick and highly absorbent making it a pleasure to use. There are 50 nose picks per pack.
We're fine with keeping it simple and not making the packaging too busy, however we're open to your ideas and designs! I have given you the most important information relevant to the project. If there are any questions or something is not clear enough please kindly message me.

Requirements
Must have
• professional looking
clean looking
not busy
Should not have
• words clumping together making it appear as too much text in one area
too much text clumped together on the design

```html
<!DOCTYPE html>
<html lang="en">
<head>
<meta charset="utf-8">
<title>Hummingfern Bramble Dabs – Cotton Swabs Label</title>
<link href="https://fonts.googleapis.com/css2?family=Montserrat:wght@400;500;700;800;900&display=swap" rel="stylesheet">
<style>
  :root {
    --teal: #85c9be;
    --teal-deep: #74b8ad;
    --charcoal: #363636;
    --ink: #000000;
    --paper: #ffffff;
  }
  * { box-sizing: border-box; margin: 0; padding: 0; }
  html, body {
    width: 1200px; height: 1001px; overflow: hidden;
    background: var(--paper);
    font-family: "Montserrat", sans-serif;
  }
  .canvas { position: relative; width: 1200px; height: 1001px; }

  .label {
    position: absolute; left: 314px; width: 572px; height: 286px;
    background: var(--teal); overflow: hidden;
  }
  .label--front { top: 153px; }
  .label--back { top: 537px; }

  /* Front */
  .brand {
    position: absolute; left: 55px; top: 42px;
    display: flex; align-items: center; gap: 7px;
  }
  .brand__dot { width: 14px; height: 14px; border-radius: 50%; background: var(--ink); flex: none; }
  .brand__name {
    font-weight: 700; font-size: 15px; line-height: 1.15; color: var(--ink);
    letter-spacing: 0.2px;
  }
  .title {
    position: absolute; left: 54px; font-weight: 800; color: var(--ink);
    line-height: 1; letter-spacing: 0.5px;
  }
  .title--cotton { top: 102px; font-size: 52px; }
  .title--swabs { top: 148px; font-size: 70px; letter-spacing: 0; }

  .site-pill {
    position: absolute; left: 55px; top: 220px; height: 25px;
    padding: 0 11px;
    background: var(--ink); border-radius: 4px;
    color: var(--paper); font-size: 12.5px; font-weight: 400; white-space: nowrap;
    display: inline-flex; align-items: center; justify-content: center;
  }

  .swab-art {
    position: absolute; left: 352px; top: 18px; width: 205px; height: 257px;
    background: linear-gradient(135deg, var(--teal) 0%, var(--teal-deep) 50%, var(--teal) 100%);
    border-radius: 12px;
  }
  .quality-seal {
    position: absolute; left: 347px; top: 52px; width: 90px; height: 90px;
    border-radius: 50%; background: var(--charcoal);
  }

  .count-tab {
    position: absolute; left: 466px; top: 189px; width: 80px; height: 97px;
    background: var(--charcoal); border-radius: 9px 9px 0 0;
    color: var(--teal); text-align: center; padding-top: 10px;
  }
  .count-tab__number { font-size: 40px; font-weight: 800; line-height: 1; }
  .count-tab__unit { font-size: 16px; font-weight: 700; line-height: 0.98; margin-top: 2px; }

  /* Back */
  .info-block { position: absolute; left: 43px; width: 364px; }
  .info-block--use { top: 52px; }
  .info-block--caution { top: 181px; }
  .info-block__heading {
    height: 23px; background: var(--charcoal); color: var(--teal);
    font-size: 13.5px; font-weight: 700; padding-left: 14px;
    display: flex; align-items: center; gap: 4px;
  }
  .info-block__heading svg { width: 12px; height: 11px; }
  .info-block__text {
    margin-top: 6px; font-size: 13.8px; line-height: 16.7px; color: var(--ink);
    text-align: justify; text-align-last: left; font-weight: 400;
    letter-spacing: -0.1px;
  }
  .info-block--caution .info-block__text { margin-top: 10px; }

  .code-frame {
    position: absolute; left: 447px; top: 46px; width: 87px; height: 196px;
    border: 1px solid var(--ink);
  }
</style>
</head>
<body>
<main class="canvas">
  <section class="label label--front">
    <div class="swab-art" role="img" aria-label="Line illustration of two crossed cotton swabs"></div>
    <div class="quality-seal"></div>

    <div class="brand">
      <span class="brand__dot"></span>
      <span class="brand__name">Hummingfern Bramble<br>Dabs</span>
    </div>

    <h1 class="title title--cotton">COTTON</h1>
    <h2 class="title title--swabs">SWABS</h2>

    <div class="site-pill">www.HummingfernBramble.example</div>

    <div class="count-tab">
      <div class="count-tab__number">50</div>
      <div class="count-tab__unit">NOSE<br>PICKS</div>
    </div>
  </section>

  <section class="label label--back">
    <div class="info-block info-block--use">
      <h3 class="info-block__heading">HOW TO USE:</h3>
      <p class="info-block__text">insert cotton nose pick into nostril and give it a few counter clock wise twirls or till you feel mucus/debris latch onto the cotton. You may need to repeat the process and use more than one nose pick to achieve desired result.</p>
    </div>

    <div class="info-block info-block--caution">
      <h3 class="info-block__heading">
        <svg viewBox="0 0 12 11" aria-hidden="true"><path d="M6 0.5 L11.6 10.5 H0.4 Z" fill="#85c9be"/><rect x="5.3" y="3.6" width="1.4" height="3.8" fill="#363636"/><rect x="5.3" y="8.2" width="1.4" height="1.3" fill="#363636"/></svg>
        CAUTION:
      </h3>
      <p class="info-block__text">Never insert plastic end of nose pick into any part of your body. Be careful and use with caution.</p>
    </div>

    <div class="code-frame"></div>
  </section>
</main>
</body>
</html>
```